PPT Design Project for an educational startup

We seek a PPT design for a new company based in Japan called "Brevonta".
We provide PPT slide-based educational videos for free.
Please see the link below. You will see some videos.
http://marvex-example.jp/
The current template is also attached.
As we are changing our service name from Marvex to Brevonta, we are considering to change the PPT template as well.
Here are some notes regarding this project.
1. We need three pages;
- Title page: Letters for the tile and the logo are necessary. Some pictorial marks or other design would be appreciated.
- Contents page: Just one line to divide the message part and contents part should be sufficient. Please do not spend your time here.
- Final page: The word "Thank you for watching!" in the center. Some pictorial marks or other design would be appreciated.
2. Please use light green, orange, and purple as main colors. (Same as the current template)
3. You don't have to think about the font-style. This is going to be Japanese font, so we will take care of this.
4. Background color needs to be white, as the slides could be printed out.
5. We use Powerpoint for Mac.
6. No copyright section required, as these slides will be creative commons. Instead of the copyright section, please put the creative commons mark in all slides. (which is in the original template attached)
Updates
Please forget about the creative commons mark.
Hi all,
Target Market(s)
16-25 years old people, who are highly educated or highly motivated for education
Industry/Entity Type
It Company
Requirements
Must have
- 1. Creative commons mark (which is in the original template)
Should not have
- 1. Copyright mark

```html
<!DOCTYPE html>
<html lang="en">
<head>
<meta charset="utf-8">
<title>Brevonta – Content Page</title>
<link rel="stylesheet" href="https://fonts.googleapis.com/css2?family=Open+Sans:wght@700&display=swap">
<style>
  :root {
    --orange: #f59e40;
    --light-green: #7cc242;
    --purple: #8a4fb0;
    --white: #ffffff;
    --rule-grey: #b5b5b5;
  }
  html, body {
    margin: 0;
    padding: 0;
    width: 1200px;
    height: 900px;
    overflow: hidden;
    background: var(--white);
  }
  .slide {
    position: relative;
    width: 1200px;
    height: 900px;
    background: var(--white);
    font-family: "Open Sans", Arial, sans-serif;
  }
  .slide-header {
    position: absolute;
    inset: 0;
  }
  .slide-title {
    position: absolute;
    left: 11px;
    top: 7px;
    margin: 0;
    color: var(--white);
    font-size: 57px;
    font-weight: 700;
    letter-spacing: 0.12em;
    line-height: 1.2;
  }
  .footer-rule {
    position: absolute;
    left: 0;
    top: 786px;
    width: 1200px;
    height: 3px;
    border-top: 1px solid var(--rule-grey);
    border-bottom: 1px solid var(--rule-grey);
    box-sizing: border-box;
  }
  .brand {
    position: absolute;
    right: 16px;
    top: 804px;
    display: flex;
    align-items: flex-start;
    gap: 6px;
  }
  .brand-name {
    margin: 0;
    color: var(--light-green);
    font-size: 50px;
    font-weight: 700;
    line-height: 1.2;
  }
  .brand-mark {
    width: 12px;
    height: 12px;
    margin-top: 12px;
    background: var(--purple);
  }
</style>
</head>
<body>
  <main class="slide">
    <svg class="slide-header" width="1200" height="900" viewBox="0 0 1200 900" aria-hidden="true">
      <path class="header-wave" fill="var(--orange)"
            d="M0 0 H1200 V377 C1100 360 960 312 833 250 C650 162 450 120 281 123 C155 125 60 140 0 153 Z"/>
      <line class="header-rule" x1="0" y1="121" x2="1196" y2="121" stroke="var(--white)" stroke-width="1.5"/>
    </svg>
    <h1 class="slide-title">Content Page</h1>
    <div class="footer-rule"></div>
    <div class="brand">
      <p class="brand-name">Brevonta</p>
      <span class="brand-mark"></span>
    </div>
  </main>
</body>
</html>
```